Business Card Design

We are a manufacturing and distribution company with most of our customer base being supermarkets. We have established brand guidelines that are attached.

```html
<!DOCTYPE html>
<html lang="en">
<head>
<meta charset="utf-8">
<title>Vantello Business Card</title>
<link rel="stylesheet" href="https://fonts.googleapis.com/css2?family=Montserrat:wght@600;800&family=Open+Sans:wght@400;600&display=swap">
<style>
  :root {
    --bg: #2a2b30;
    --card-white: #ffffff;
    --card-dark: #221f20;
    --ink: #141414;
    --brand-red: #e31b23;
    --brand-blue: #0a6cb3;
    --white: #ffffff;
  }
  * { box-sizing: border-box; margin: 0; padding: 0; }
  html, body {
    width: 1200px; height: 800px; overflow: hidden;
    background: var(--bg);
  }
  .canvas {
    position: relative; width: 1200px; height: 800px;
  }
  .card {
    position: absolute; top: 250px;
    width: 520px; height: 300px;
    border-radius: 18px; overflow: hidden;
  }
  .card-front { left: 60px; background: var(--card-white); }
  .card-back { left: 620px; background: var(--card-dark); }

  .front-bands { position: absolute; inset: 0; }

  .wordmark {
    font-family: "Montserrat", sans-serif; font-weight: 800;
    letter-spacing: 1px; color: var(--ink);
  }
  .card-front .wordmark {
    position: absolute; left: 36px; top: 44px; font-size: 30px;
  }

  .person { position: absolute; left: 36px; top: 150px; width: 290px; }
  .person-name {
    font-family: "Montserrat", sans-serif; font-weight: 800;
    font-size: 20px; color: var(--ink);
  }
  .person-title {
    font-family: "Montserrat", sans-serif; font-weight: 600;
    font-size: 13px; color: var(--brand-blue); margin-top: 2px;
  }
  .person-rule {
    height: 1px; background: var(--brand-red); margin: 8px 0 8px;
  }
  .contact-list { list-style: none; }
  .contact-item {
    display: flex; align-items: center; gap: 9px;
    font-family: "Open Sans", sans-serif; font-size: 12px;
    color: var(--ink); line-height: 19px;
  }
  .contact-icon { width: 11px; height: 11px; flex: none; }

  .address {
    position: absolute; right: 34px; top: 120px; width: 165px;
    border-top: 1px solid var(--brand-blue); padding-top: 8px;
    font-family: "Open Sans", sans-serif; font-size: 11.5px;
    line-height: 16px; color: var(--ink);
  }

  .back-brand {
    position: absolute; inset: 0;
    display: flex; align-items: center; justify-content: center; gap: 14px;
  }
  .back-square {
    width: 26px; height: 26px; background: var(--brand-red);
  }
  .card-back .wordmark { color: var(--white); font-size: 34px; letter-spacing: 2px; }
</style>
</head>
<body>
<main class="canvas">

  <section class="card card-front" aria-label="Business card front">
    <svg class="front-bands" viewBox="0 0 520 300" width="520" height="300" aria-hidden="true">
      <polygon points="0,300 0,292 430,252 520,252 520,300" fill="var(--brand-red)"/>
      <polygon points="430,252 520,178 520,252" fill="var(--brand-blue)"/>
    </svg>

    <div class="wordmark">VANTELLO</div>

    <div class="person">
      <div class="person-name">Marcus Delaney</div>
      <div class="person-title">CEO/Founder</div>
      <div class="person-rule"></div>
      <ul class="contact-list">
        <li class="contact-item">
          <svg class="contact-icon" viewBox="0 0 12 12" aria-hidden="true"><path d="M2.5 1 L4.5 1 L5.2 3.6 L3.9 4.6 Q5 7 7.4 8.1 L8.4 6.8 L11 7.5 L11 9.5 Q11 11 9.5 11 Q1 10 1 2.5 Q1 1 2.5 1 Z" fill="var(--brand-red)"/></svg>
          555-013-2847
        </li>
        <li class="contact-item">
          <svg class="contact-icon" viewBox="0 0 12 12" aria-hidden="true"><rect x="0.5" y="2" width="11" height="8" fill="var(--brand-red)"/><path d="M0.5 2 L6 6.5 L11.5 2" stroke="#fff" stroke-width="1" fill="none"/></svg>
          marcus@mailsample.com
        </li>
        <li class="contact-item">
          <svg class="contact-icon" viewBox="0 0 12 12" aria-hidden="true"><circle cx="6" cy="6" r="5.5" fill="var(--brand-red)"/><path d="M0.5 6 H11.5 M6 0.5 V11.5 M2 3.3 H10 M2 8.7 H10" stroke="#fff" stroke-width="0.8"/><ellipse cx="6" cy="6" rx="2.4" ry="5.5" stroke="#fff" stroke-width="0.8" fill="none"/></svg>
          www.vantellofoods.com
        </li>
      </ul>
    </div>

    <address class="address">
      418 Harbor Lane<br>
      Suite 200, Lakeview<br>
      MI 49000
    </address>
  </section>

  <section class="card card-back" aria-label="Business card back">
    <div class="back-brand">
      <span class="back-square"></span>
      <span class="wordmark">VANTELLO</span>
    </div>
  </section>

</main>
</body>
</html>
```